Simple design for eCommerce retailer of Custom Cut Mirror Frames

We need a fresh design for our eCommerce store. Currently, we need a design for each page on the existing site.

Here is the site as it stands right now: glassvela.com

Here is a competitor site that we like. The owner really likes the block look for the home page: framorly.com

Here is a video we would like to feature: https://videohost.example/v/Kp7rTq2LmXa

Here is the color palate, emphasis on the green and purple: https://palettes.example/quiet-bay-theme-48271953/?showPublished=true

Here is an example of a landing page we are currently using: https://glassvela.com/lander-10-off-install/

Font for the site should be the google font Lato

Home page should include the following sections/blocks:

How it works
Shop now
Testimonials
Featured Products
Before and After Gallery
Updates

My team has been slow getting back to me with feedback. I'm pushing them to speed their process up.

Target Market(s)

Women, Ages 35-65+

Number of Pages Required

5+ page

Font styles to use
Sans Serif

Requirements
Must have
• -Before and after gallery
• -Star ratings
• -eCommerce look and feel
• -Info about being able to order free samples
• -Language from the checkmarks on the landing page
• -sleek product page
• -home page should be have a very modern design feel
Should not have
• Product Prices...the user has to use the calculator to determine the price of their purchase.
• Sliders

```html
<!DOCTYPE html>
<html lang="en">
<head>
<meta charset="utf-8">
<title>GlassVela – Custom Mirror Frames</title>
<link href="https://fonts.googleapis.com/css2?family=Poppins:wght@300;400;500;600;700&display=swap" rel="stylesheet">
<style>
:root{
  --purple:#c39bd3;
  --purple-dark:#a97fbf;
  --teal:#86c7b8;
  --teal-dark:#5fae9c;
  --ink:#222;
  --text:#555;
  --muted:#8a8a8a;
  --line:#e3e3e3;
  --soft:#f4f4f4;
  --black:#111;
  --footer:#2d2d2d;
  --footer-deep:#1f1f1f;
  --white:#fff;
}
*{box-sizing:border-box;margin:0;padding:0}
html,body{width:1200px;height:4918px;overflow:hidden}
body{position:relative;font-family:'Poppins',sans-serif;color:var(--text);background:var(--white)}
.abs{position:absolute}
.btn{position:absolute;background:var(--purple);color:var(--white);font-size:13px;font-weight:500;display:flex;align-items:center;justify-content:center;border-radius:2px}
.h2{position:absolute;left:0;width:1200px;text-align:center;font-size:34px;font-weight:400;color:var(--ink)}

.topbar{left:0;top:0;width:1200px;height:33px;background:var(--black);color:var(--white);font-size:11px}
.topbar .lead{position:absolute;left:144px;top:9px}
.topbar .util{position:absolute;right:144px;top:9px;display:flex;gap:18px}

.logo{left:144px;top:68px}
.logo .name{font-size:26px;font-weight:600;color:#444;display:flex;align-items:center;gap:8px}
.logo .name i{width:12px;height:12px;background:var(--purple);display:block}
.search{left:470px;top:73px;width:430px;height:36px;display:flex;border:1px solid var(--line)}
.search .cat{width:110px;background:var(--purple);color:var(--white);font-size:11px;display:flex;align-items:center;padding-left:12px}
.search .field{flex:1;font-size:11px;color:var(--muted);display:flex;align-items:center;padding-left:12px}
.search .go{width:40px;background:var(--purple);display:flex;align-items:center;justify-content:center}
.cart{left:945px;top:76px;display:flex;gap:8px;align-items:center}
.cart .t{font-size:10px;color:var(--ink);font-weight:600;line-height:1.3}
.cart .t span{display:block;font-weight:400;color:var(--muted)}
.nav{left:144px;top:140px;width:912px;height:32px;display:flex;justify-content:space-between;padding:0 16px;font-size:12px;color:var(--ink);border-bottom:1px solid var(--line)}
.nav a{text-decoration:none;color:inherit;padding-top:6px}
.nav a.on{color:var(--purple);border-bottom:2px solid var(--purple)}

.hero{left:0;top:180px;width:1200px;height:525px;background:linear-gradient(90deg,#a9adb2 0%,#c7c9cb 35%,#dcdad6 60%,#8c7a68 80%,#e6e3de 100%)}
.hero h1{position:absolute;left:144px;top:150px;width:470px;font-size:37px;line-height:1.32;font-weight:600;color:var(--white)}

.press{left:0;top:715px;width:1200px;height:105px;background:var(--soft);display:flex;align-items:center;justify-content:space-between;padding:0 140px}
.press span{font-size:18px;font-weight:600;color:#b5b5b5}

.checks{left:144px;top:1012px;list-style:none;font-size:13px;color:var(--ink)}
.checks li{display:flex;align-items:center;gap:10px;height:33px}
.video{left:541px;top:1007px;width:515px;height:354px;background:linear-gradient(110deg,#d8d1c6,#b9ab98 45%,#3d4a6a 70%,#cfc6ba)}
.video .bar{position:absolute;left:0;bottom:0;width:100%;height:24px;background:rgba(0,0,0,.75)}

.feat-title{left:144px;top:1513px;font-size:24px;font-weight:500;color:var(--ink)}
.feat-line{left:144px;top:1560px;width:912px;height:1px;background:var(--line)}
.arrows{left:1006px;top:1520px;display:flex;gap:4px}
.arrows b{width:22px;height:22px;border:1px solid var(--line);display:flex;align-items:center;justify-content:center;font-size:11px;color:var(--muted);font-weight:400}
.prod{position:absolute;width:216px}
.prod .ph{width:216px;height:220px;background:linear-gradient(135deg,#d9dcdb,#b7bcbb)}
.prod .lbl{text-align:center;font-size:12.5px;color:var(--ink);margin-top:10px;line-height:1.35}
.ov{position:absolute;left:0;top:0;width:216px;height:280px;background:rgba(40,40,40,.92);color:var(--white);text-align:center;padding-top:70px;font-size:13px}
.ov .stars{color:#f5c242;margin:8px 0;letter-spacing:2px}
.ov .s{display:inline-block;background:var(--purple);padding:5px 14px;font-size:11px;margin-top:8px}
.ov .a{font-size:11px;margin-top:10px}

.reviews{left:0;top:2345px;width:1200px;height:590px;background:var(--soft)}
.card{position:absolute;top:180px;width:276px;height:263px;background:var(--white);box-shadow:0 2px 8px rgba(0,0,0,.08);text-align:center;padding:20px 22px}
.card .av{width:64px;height:64px;border-radius:50%;margin:0 auto;background:linear-gradient(135deg,#e8d6c8,#b99a86)}
.card .stars{color:#f5c242;letter-spacing:2px;font-size:14px;margin-top:14px}
.card .who{color:var(--purple);font-size:13px;margin-top:4px}
.card p{font-size:11.5px;line-height:1.6;margin-top:10px}
.count{left:0;top:2820px;width:1200px;text-align:center;font-size:27px;color:var(--ink)}

.band{left:144px;top:2935px;width:912px;height:76px}
.band .item{position:absolute;top:0;height:76px;display:flex;align-items:center;gap:12px;font-size:13px;color:var(--ink);line-height:1.35}
.band .ic{width:44px;height:44px;border-radius:50%;border:2px solid var(--white);flex:none}

.gal{position:absolute;background:linear-gradient(135deg,#e9e3da,#b5a792)}
.tag-b,.tag-a{position:absolute;height:30px;display:flex;align-items:center;justify-content:center;font-size:14px;color:var(--ink)}
.tag-b{background:rgba(195,155,211,.85)}
.tag-a{background:rgba(134,199,184,.9)}

.large{left:144px;top:3772px;width:912px;height:131px;border:1px solid var(--teal);display:flex;align-items:center}
.large h3{width:260px;padding-left:70px;font-size:24px;font-weight:400;color:var(--ink);line-height:1.2}
.large .div{width:1px;height:90px;background:var(--teal)}
.large .body{padding-left:24px;font-size:13px;color:var(--ink);line-height:1.5;width:600px}
.large .body b{font-size:11px;font-weight:600}
.large .body em{font-style:normal;color:var(--purple)}

.promo{left:0;top:3991px;width:1200px;height:404px;background:linear-gradient(90deg,#5b5450 0%,#c9c3bc 30%,#a9a39e 50%,#e4e1dc 75%,#d3cfc9 100%)}
.seal{left:690px;top:4030px;width:104px;height:104px;border-radius:50%;background:var(--purple);color:var(--white);text-align:center;font-size:9px;display:flex;flex-direction:column;justify-content:center;line-height:1.25}
.seal b{font-size:16px;font-weight:700}
.promo-h{left:636px;top:4185px;width:420px;text-align:right;font-size:29px;line-height:1.35;color:var(--purple-dark)}

.nl-t{left:144px;top:4460px;font-size:15px;font-weight:600;color:var(--ink)}
.nl-s{left:144px;top:4484px;font-size:10px;width:260px}
.nl-in{left:440px;top:4468px;width:285px;height:36px;border:1px solid var(--line);font-size:11px;color:var(--muted);padding:10px 12px}
.social{left:966px;top:4474px;display:flex;gap:6px}
.social i{width:24px;height:24px;background:var(--purple);display:block}

.footer{left:0;top:4582px;width:1200px;height:272px;background:var(--footer);color:#ddd;font-size:12px}
.col{position:absolute;top:30px;line-height:1.75}
.col h4{color:var(--white);font-size:13px;font-weight:600;border-bottom:1px solid #555;padding-bottom:6px;margin-bottom:8px}
.pay{display:flex;gap:6px;margin-top:8px}
.pay i{width:34px;height:22px;background:#ccc;display:block;border-radius:3px}
.seal2{width:90px;height:30px;background:var(--teal);border-radius:3px}
.flogo{position:absolute;left:840px;top:130px;font-size:28px;font-weight:600;color:var(--white)}
.legal{left:0;top:4854px;width:1200px;height:64px;background:var(--footer-deep);color:#aaa;font-size:10px}
</style>
</head>
<body>

<div class="abs topbar">
  <div class="lead">In San Diego, or South Orange County? Free In-Home Consultation</div>
  <div class="util"><span>(760) 555-0187</span><span>Register</span><span>Login</span></div>
</div>

<div class="abs logo">
  <div class="name"><i></i>GlassVela</div>
</div>
<div class="abs search">
  <div class="cat">All Categories ▾</div>
  <div class="field">I'm Searching for...</div>
  <div class="go"><svg width="16" height="16" viewBox="0 0 16 16"><circle cx="7" cy="7" r="5" fill="none" stroke="#fff" stroke-width="2"/><line x1="11" y1="11" x2="15" y2="15" stroke="#fff" stroke-width="2"/></svg></div>
</div>
<div class="abs cart">
  <svg width="26" height="24" viewBox="0 0 26 24"><path d="M1 2h4l3 13h14l3-9H7" fill="none" stroke="#c39bd3" stroke-width="2"/><circle cx="10" cy="20" r="2" fill="#c39bd3"/><circle cx="20" cy="20" r="2" fill="#c39bd3"/></svg>
  <div class="t">SHOPPING CART<span>0 items · $0.00</span></div>
</div>
<nav class="abs nav">
  <a class="on">Home</a><a>Shop Mirror Frames</a><a>Custom Framed Mirrors</a><a>How it Works</a><a>Before &amp; After Gallery</a><a>Contact Us</a>
</nav>

<section class="abs hero" role="img" aria-label="Woman hanging a dark framed mirror above a bathroom vanity">
  <h1>We Offer Frames That Look Wonderful And Assemble And Install Easily.</h1>
  <div class="btn" style="left:144px;top:400px;width:140px;height:40px">Shop Today</div>
</section>

<div class="abs press">
  <span>Nest &amp; Hearth</span><span>Roomwise</span><span>Linen Lane</span><span>Porchlight</span><span>Cedar Post</span><span>Tilework Weekly</span>
</div>

<h2 class="h2" style="top:925px">How it Works</h2>
<ul class="abs checks">
  <li><svg width="16" height="16"><path d="M2 8l4 4 8-9" fill="none" stroke="#86c7b8" stroke-width="2.5"/></svg>DIY mirror framing kit</li>
  <li><svg width="16" height="16"><path d="M2 8l4 4 8-9" fill="none" stroke="#86c7b8" stroke-width="2.5"/></svg>Install with mirror still on wall</li>
  <li><svg width="16" height="16"><path d="M2 8l4 4 8-9" fill="none" stroke="#86c7b8" stroke-width="2.5"/></svg>Style selections to match any home decor</li>
  <li><svg width="16" height="16"><path d="M2 8l4 4 8-9" fill="none" stroke="#86c7b8" stroke-width="2.5"/></svg>Beveled Mirrors? No problem!</li>
  <li><svg width="16" height="16"><path d="M2 8l4 4 8-9" fill="none" stroke="#86c7b8" stroke-width="2.5"/></svg>DIY install within minutes</li>
  <li><svg width="16" height="16"><path d="M2 8l4 4 8-9" fill="none" stroke="#86c7b8" stroke-width="2.5"/></svg>Guaranteed to fit any mirror, any size</li>
  <li><svg width="16" height="16"><path d="M2 8l4 4 8-9" fill="none" stroke="#86c7b8" stroke-width="2.5"/></svg>Extends beyond mirror to hide ugly edges</li>
  <li><svg width="16" height="16"><path d="M2 8l4 4 8-9" fill="none" stroke="#86c7b8" stroke-width="2.5"/></svg>BEFORE &amp; AFTER GALLERY</li>
  <li><svg width="16" height="16"><path d="M2 8l4 4 8-9" fill="none" stroke="#86c7b8" stroke-width="2.5"/></svg>100% Satisfaction Guarantee</li>
  <li><svg width="16" height="16"><path d="M2 8l4 4 8-9" fill="none" stroke="#86c7b8" stroke-width="2.5"/></svg>Outstanding customer support</li>
</ul>
<div class="abs video" role="img" aria-label="Video still of a woman presenting a framed bathroom mirror"><div class="bar"></div></div>
<div class="btn" style="left:144px;top:1386px;width:124px;height:36px">Get Started</div>

<div class="abs feat-title">Featured Products</div>
<div class="abs arrows"><b>‹</b><b>›</b></div>
<div class="abs feat-line"></div>

<div class="prod" style="left:144px;top:1607px"><div class="ph" role="img" aria-label="Sienna Umber frame corner sample"></div><div class="lbl">Sienna Umber<br>Olde World Look</div>
  <div class="ov">Sienna Umber<br>Olde World Look<div class="stars">★★★★★</div><div class="s">Shop This Frame</div><div class="a">Shop All Frames</div></div></div>
<div class="prod" style="left:376px;top:1607px"><div class="ph" role="img" aria-label="Modern Pewter frame corner sample"></div><div class="lbl">Modern Pewter<br>Modern Look</div></div>
<div class="prod" style="left:608px;top:1607px"><div class="ph" role="img" aria-label="Harbor Walnut frame corner sample" style="background:linear-gradient(135deg,#dfe1e0,#3a2a22)"></div><div class="lbl">Harbor Walnut<br>Modern Look</div></div>
<div class="prod" style="left:840px;top:1607px"><div class="ph" role="img" aria-label="Coastal Bronze frame corner sample" style="background:linear-gradient(135deg,#dcdedd,#6b4b38)"></div><div class="lbl">Coastal Bronze<br>Elegant Look</div></div>

<div class="prod" style="left:144px;top:1928px"><div class="ph" role="img" aria-label="Coastal Bronze frame corner sample" style="background:linear-gradient(135deg,#dcdedd,#6b4b38)"></div><div class="lbl">Coastal Bronze<br>Elegant Look</div></div>
<div class="prod" style="left:376px;top:1928px"><div class="ph" role="img" aria-label="Harbor Walnut frame corner sample" style="background:linear-gradient(135deg,#dfe1e0,#3a2a22)"></div><div class="lbl">Harbor Walnut<br>Modern Look</div></div>
<div class="prod" style="left:608px;top:1928px"><div class="ph" role="img" aria-label="Modern Pewter frame corner sample"></div><div class="lbl">Modern Pewter<br>Modern Look</div></div>
<div class="prod" style="left:840px;top:1928px"><div class="ph" role="img" aria-label="Sienna Umber frame corner sample" style="background:linear-gradient(135deg,#dcdedd,#2f2b28)"></div><div class="lbl">Sienna Umber<br>Olde World Look</div></div>
<div class="btn" style="left:525px;top:2232px;width:150px;height:36px">View All Frames</div>

<section class="abs reviews">
  <h2 class="h2" style="top:85px;font-size:30px">Happy Customer Reviews</h2>
  <div class="card" style="left:157px"><div class="av" role="img" aria-label="Customer portrait"></div><div class="stars">★★★★★</div><div class="who">Kerry D., Carlsbad, CA</div><p>Great product and great service! Adding frames to our mirrors made all the difference in how the master bath looks. You can't beat GlassVela for the money!</p></div>
  <div class="card" style="left:462px"><div class="av" role="img" aria-label="Customer portrait"></div><div class="stars">★★★★★</div><div class="who">Lena M., Murrieta, CA</div><p>We were so happy with the first two frames we purchased, we purchased a frame for our other bathroom. I would highly recommend this company.</p></div>
  <div class="card" style="left:767px"><div class="av" role="img" aria-label="Customer portrait"></div><div class="stars">★★★★★</div><div class="who">Dana L., Oceanside, CA</div><p>Said my three bathrooms and couldn't be happier, what a difference the new frames made! Do yourself a favor and frame your mirrors, you'll be happy you did.</p></div>
</section>
<div class="abs count">Over 3,000 5-Star Reviews</div>

<div class="abs band">
  <svg class="abs" width="912" height="76" viewBox="0 0 912 76" style="left:0;top:0">
    <polygon points="0,0 290,0 316,38 290,76 0,76" fill="#c39bd3"/>
    <polygon points="296,0 596,0 622,38 596,76 296,76 322,38" fill="#86c7b8"/>
    <polygon points="602,0 912,0 912,76 602,76 628,38" fill="#c39bd3"/>
  </svg>
  <div class="item" style="left:24px"><span class="ic" style="background:#fff"></span>100%<br>Satisfaction Guarantee</div>
  <div class="item" style="left:340px"><span class="ic"></span>See How Easy It Is - To<br>Install Custom Frames</div>
  <div class="item" style="left:650px"><span class="ic"></span>Quick And<br>Easy Installation</div>
</div>

<h2 class="h2" style="top:3120px;font-size:30px">Before &amp; After Gallery</h2>
<div class="gal" style="left:144px;top:3207px;width:282px;height:205px" role="img" aria-label="Bathroom mirror before framing"></div>
<div class="tag-b" style="left:144px;top:3382px;width:282px">Before</div>
<div class="gal" style="left:144px;top:3422px;width:282px;height:212px;background:linear-gradient(135deg,#d6cbbd,#6d5a48)" role="img" aria-label="Bathroom mirror after framing"></div>
<div class="tag-a" style="left:144px;top:3422px;width:282px">After</div>

<div class="gal" style="left:459px;top:3207px;width:137px;height:205px" role="img" aria-label="Vanity mirror before framing"></div>
<div class="gal" style="left:604px;top:3207px;width:137px;height:205px;background:linear-gradient(135deg,#d6cbbd,#6d5a48)" role="img" aria-label="Vanity mirror after framing"></div>
<div class="tag-b" style="left:459px;top:3382px;width:137px">Before</div>
<div class="tag-a" style="left:604px;top:3382px;width:137px">After</div>
<div class="gal" style="left:459px;top:3422px;width:137px;height:212px;background:linear-gradient(135deg,#e2c9a3,#8a6a44)" role="img" aria-label="Powder room mirror before framing"></div>
<div class="gal" style="left:604px;top:3422px;width:137px;height:212px;background:linear-gradient(135deg,#e0c59b,#5a4330)" role="img" aria-label="Powder room mirror after framing"></div>
<div class="tag-b" style="left:459px;top:3604px;width:137px">Before</div>
<div class="tag-a" style="left:604px;top:3604px;width:137px">After</div>

<div class="gal" style="left:774px;top:3207px;width:282px;height:205px;background:linear-gradient(135deg,#eef0f1,#a9b2b8)" role="img" aria-label="Double vanity mirror before framing"></div>
<div class="tag-b" style="left:774px;top:3382px;width:282px">Before</div>
<div class="gal" style="left:774px;top:3422px;width:282px;height:212px;background:linear-gradient(135deg,#e8e6e2,#3c3029)" role="img" aria-label="Double vanity mirror after framing"></div>
<div class="tag-a" style="left:774px;top:3422px;width:282px">After</div>
<div class="btn" style="left:560px;top:3668px;width:80px;height:34px">View All</div>

<div class="abs large">
  <h3>Large Or<br>Unique Frames?</h3>
  <div class="div"></div>
  <div class="body"><b>WE HAVE YOU COVERED!</b><br>We know that not all mirrors are created equal...in size. So if you have a large or unique mirror we have you covered. Literally!<br><em>Read on to discover how.</em></div>
</div>

<section class="abs promo" role="img" aria-label="Woman smiling beside a newly framed bathroom mirror">
  <div class="btn" style="left:946px;top:305px;width:110px;height:36px">Shop Today</div>
</section>
<div class="abs seal">Get up to 7<b>FREE<br>SAMPLES</b>limited time offer</div>
<div class="abs promo-h">Get Up To 7 Free<br>Samples For A Limited Time!</div>

<div class="abs nl-t">Be The First To Know</div>
<div class="abs nl-s">Join our Email List &amp; Receive 10% Off Your First Purchase*</div>
<div class="abs nl-in">Email Address</div>
<div class="btn" style="left:735px;top:4468px;width:125px;height:36px">SUBSCRIBE</div>
<div class="abs social"><i></i><i></i><i></i></div>

<footer class="abs footer">
  <div class="col" style="left:144px"><h4>Quick Links</h4>Home<br>Shop Mirror Frames<br>Custom Framed Mirrors<br>How it Works<br>Before &amp; After Gallery<br>Contact Us</div>
  <div class="col" style="left:355px"><h4>Contact Details</h4>4120 Harbor Lane, Suite B<br>Fairview, NC 28730<br>(866) 555-0142<br>info@framorly.com</div>
  <div class="col" style="left:632px"><h4>We Gladly Accept</h4><div class="seal2"></div><div class="pay"><i></i><i></i><i></i><i></i></div></div>
  <div class="flogo">GlassVela</div>
</footer>
<div class="abs legal">
  <div class="abs" style="left:0;top:10px;width:1200px;text-align:center">Protected under one or more of the following: U.S. Pat. Nos. 7,112,408; 8,204,517 and 7,658,231. Canadian Pat. No. 2,468,115</div>
  <div class="abs" style="left:144px;top:36px">© 2019 Northlane Co. All Rights Reserved</div>
  <div class="abs" style="right:144px;top:36px">Policies | Privacy | Security</div>
</div>

</body>
</html>
```